Pilates trainer needs new website

Summary: I need a new, meaningful website in a 1-page format, but one that can be expanded if necessary. I teach in various studios and in the future also in companies. Therefore, the website should convey growth, joy, uniqueness, workout and a bit of luxury.
The website should be inviting.
Layout:
Introduction what I offer
A bit about me
Option to upload price list and timetable in PDF format
Studio address where I teach
The color scheme should be petrol, gold, and colors that match. Not too dark, please.
My current website www.movewell-brennach.de, new domain is corebalance-studio.com (I have already purchased it)
Logo file attached
I have attached a few suggestions but I am also happy to be surprised.

Target Market(s)

Pilates private and small groups,

Industry/Entity Type

Pilates teacher freelancer

Coding

Coded - Design and coding required

Number of Pages Required

1 page

Requirements
Must have
• Welcoming appearance, about me, pictures, offers, colors from the logo but don't get do dark, more fresh and a bit luxurious
Should not have
• Not too wild and going crazy with colors

```html
<!DOCTYPE html>
<html lang="en">
<head>
<meta charset="utf-8">
<title>Lena Marwick – Pilates Studio Trainer</title>
<link href="https://fonts.googleapis.com/css2?family=Parisienne&family=Lato:wght@300;400;700&family=Playfair+Display:ital,wght@0,400;1,400&display=swap" rel="stylesheet">
<style>
:root{
  --gold:#c49a45;
  --gold-light:#e2c27a;
  --gold-dark:#9b7430;
  --brown:#2c2118;
  --brown-mid:#4a3828;
  --cream:#f7f0e3;
  --cream-deep:#efe3cc;
  --text:#3b3129;
  --muted:#7b6e62;
  --white:#ffffff;
}
*{box-sizing:border-box;margin:0;padding:0}
html,body{width:1200px;height:3684px;overflow:hidden}
body{font-family:"Lato",sans-serif;color:var(--text);background:var(--white);font-size:13px;line-height:1.6;position:relative}
.section-title{font-family:"Parisienne",cursive;color:var(--gold);font-size:50px;text-align:center;line-height:1}
.title-rule{display:block;margin:6px auto 0;width:180px;height:10px}
.btn{display:inline-block;padding:9px 26px;border-radius:20px;background:linear-gradient(90deg,var(--gold-dark),var(--gold-light),var(--gold-dark));color:var(--white);font-size:10px;letter-spacing:1.5px;text-transform:uppercase;font-weight:700}
.photo{display:block}

/* Hero */
.hero{position:absolute;top:0;left:0;width:1200px;height:760px;overflow:hidden}
.hero-photo{position:absolute;inset:0;background:radial-gradient(ellipse at 60% 40%,#6b5742 0%,#3b2d20 55%,#1f1710 100%)}
.hero-shade{position:absolute;inset:0;background:linear-gradient(180deg,rgba(20,14,9,.35),rgba(20,14,9,.55))}
.nav{position:absolute;top:18px;left:150px;right:150px;display:flex;align-items:center;justify-content:space-between}
.brand{display:flex;align-items:center;gap:10px;color:var(--gold-light);font-weight:700;font-size:14px;letter-spacing:1px}
.brand-dot{width:46px;height:46px;border-radius:50%;border:2px solid var(--gold)}
.nav-links{display:flex;gap:30px;align-items:center;color:var(--white);font-size:10px;letter-spacing:1.5px}
.hero-copy{position:absolute;top:160px;left:0;width:1200px;text-align:center;color:var(--white)}
.hero-kicker{font-size:17px;letter-spacing:3px;text-transform:uppercase;line-height:1.5}
.hero-name{font-family:"Parisienne",cursive;font-size:62px;color:var(--white);line-height:1.15;margin-top:14px}
.hero-buttons{margin-top:26px;display:flex;flex-direction:column;align-items:center;gap:10px}
.hero-wave{position:absolute;left:0;bottom:0;width:1200px;height:170px}

/* Offer */
.offer{position:absolute;top:745px;left:0;width:1200px;height:265px;text-align:center}
.offer p{width:760px;margin:10px auto 0;font-size:12px;line-height:1.55;color:var(--text)}
.offer .btn{margin-top:16px}
.side-tab{position:absolute;top:672px;right:0;width:178px;height:110px;display:flex;background:var(--white);box-shadow:0 4px 18px rgba(0,0,0,.18);z-index:3}
.side-tab-body{flex:1;padding:10px 12px;font-size:10px}
.side-tab-body strong{display:block;font-size:11px}
.side-tab-body .price{color:var(--gold);font-weight:700;margin-top:16px;font-size:12px}
.side-tab-label{width:34px;background:var(--gold);color:var(--white);writing-mode:vertical-rl;text-align:center;font-size:10px;letter-spacing:2px;font-weight:700}

/* About */
.about{position:absolute;top:1010px;left:0;width:1200px;height:550px;background:var(--cream)}
.about-wave-top{position:absolute;top:-1px;left:0;width:1200px;height:40px}
.about-photo{position:absolute;top:70px;left:152px;width:400px;height:430px;background:linear-gradient(160deg,#8a7560,#4b3b2c);box-shadow:0 6px 20px rgba(0,0,0,.2)}
.about-caption{position:absolute;top:390px;left:152px;width:230px;padding:12px 16px;background:rgba(44,33,24,.85)}
.about-caption b{display:block;font-size:14px;color:var(--gold-light)}
.about-caption span{font-size:9px;letter-spacing:1px;text-transform:uppercase;color:var(--white)}
.about-text{position:absolute;top:70px;left:628px;width:420px}
.about-text .section-title{text-align:left}
.about-text h3{font-family:"Playfair Display",serif;font-size:20px;font-weight:400;margin-top:12px}
.about-text p{font-size:12px;margin-top:6px;line-height:1.55}
.about-text .btn{margin-top:12px}
.about-photo-2{position:absolute;top:380px;left:640px;width:408px;height:150px;background:linear-gradient(150deg,#b9a58a,#6d5a46);box-shadow:0 6px 20px rgba(0,0,0,.2)}

/* Prices */
.prices{position:absolute;top:1560px;left:0;width:1200px;height:640px;background:var(--white)}
.prices .section-title{margin-top:108px}
.price-grid{position:absolute;top:190px;left:150px;width:900px;display:grid;grid-template-columns:repeat(4,1fr);gap:12px}
.price-card{height:272px;background:var(--white);box-shadow:0 4px 16px rgba(0,0,0,.12);padding:16px;border-top:3px solid var(--gold)}
.price-card h4{font-family:"Playfair Display",serif;font-weight:400;color:var(--gold);font-size:20px;line-height:1.15}
.price-card .item{margin-top:12px;font-size:10px;line-height:1.45}
.price-card .item b{display:block;font-size:11px}
.price-card .amount{color:var(--gold);font-weight:700;font-size:12px;margin-top:4px;display:block}
.price-buttons{position:absolute;top:518px;left:0;width:1200px;display:flex;justify-content:center;gap:14px}

/* Testimonials */
.testimonials{position:absolute;top:2200px;left:0;width:1200px;height:580px;background:var(--cream)}
.testimonials .section-title{margin-top:70px}
.quotes{position:absolute;top:160px;left:180px;width:840px;display:grid;grid-template-columns:1fr 1fr;gap:50px}
.quote{text-align:center;font-size:11px;font-style:italic}
.quote-mark{font-family:"Playfair Display",serif;font-size:60px;color:var(--gold);line-height:.6;font-style:normal;display:flex;align-items:center;gap:12px;justify-content:center}
.quote-mark small{font-family:"Lato",sans-serif;font-size:10px;color:var(--muted);font-style:normal}
.quote p{margin-top:20px}
.author{display:flex;align-items:center;justify-content:center;gap:10px;margin-top:18px;font-style:normal}
.author-dot{width:34px;height:34px;border-radius:50%;background:var(--cream-deep);border:2px solid var(--gold)}
.author b{display:block;font-size:12px}
.author span{font-size:9px;color:var(--muted)}
.testimonials .more{position:absolute;top:380px;left:0;width:1200px;text-align:center}
.test-wave{position:absolute;bottom:-1px;left:0;width:1200px;height:60px}

/* Training */
.training{position:absolute;top:2780px;left:0;width:1200px;height:540px;background:var(--white)}
.training-photo{position:absolute;top:70px;left:180px;width:400px;height:190px;background:linear-gradient(120deg,#cfc3b3,#7d6a56)}
.training-text{position:absolute;top:100px;left:620px;width:420px}
.training h3{font-family:"Playfair Display",serif;font-weight:400;font-size:17px;margin-bottom:8px}
.training ul{list-style:none;font-size:11px}
.training li{padding-left:12px;position:relative;line-height:1.7}
.training li:before{content:"";position:absolute;left:0;top:8px;width:4px;height:4px;background:var(--gold);border-radius:50%}
.skills{position:absolute;top:300px;left:180px;width:420px}
.training-photo-2{position:absolute;top:280px;left:720px;width:330px;height:200px;background:linear-gradient(140deg,#6a5644,#2f241a)}

/* Footer */
.footer{position:absolute;top:3320px;left:0;width:1200px;height:364px;background:var(--brown);color:#d8cbb8}
.footer-wave{position:absolute;top:-40px;left:0;width:1200px;height:60px}
.footer-logo{position:absolute;top:-46px;left:550px;width:100px;height:100px;border-radius:50%;background:var(--brown);border:2px solid var(--gold);display:flex;align-items:center;justify-content:center;color:var(--gold-light);font-weight:700;font-size:11px;letter-spacing:1px;text-align:center;line-height:1.2}
.footer-cols{position:absolute;top:150px;left:150px;width:900px;display:grid;grid-template-columns:1.3fr 1fr 1fr .7fr .8fr;gap:20px;font-size:10px}
.footer h5{font-family:"Parisienne",cursive;color:var(--gold);font-size:24px;font-weight:400;line-height:1}
.footer h6{color:var(--gold-light);font-size:10px;letter-spacing:1px;text-transform:uppercase;margin-bottom:6px}
.footer p{line-height:1.6}
.contact-line{display:flex;align-items:center;gap:6px;margin-top:4px}
.contact-line svg{width:11px;height:11px;flex:none}
.badge{width:90px;height:100px;background:linear-gradient(160deg,#3a6f7a,#1f4a52);border:2px solid var(--gold)}
.footer-bottom{position:absolute;bottom:0;left:0;width:1200px;height:34px;border-top:1px solid rgba(196,154,69,.4);display:flex;align-items:center;justify-content:space-between;padding:0 150px;font-size:9px;color:#a99a86}
.socials{display:flex;gap:8px}
.socials i{width:12px;height:12px;border-radius:50%;background:var(--gold);display:block}
</style>
</head>
<body>

<header class="hero">
  <div class="hero-photo photo" role="img" aria-label="Dim Pilates studio interior with reformer machines"></div>
  <div class="hero-shade"></div>
  <nav class="nav">
    <div class="brand"><span class="brand-dot"></span>Corebalance Studio</div>
    <div class="nav-links"><span>HOME</span><span>TRAININGS</span><span>ABOUT ME</span><span class="btn">Contact</span></div>
  </nav>
  <div class="hero-copy">
    <div class="hero-kicker">Change happens through movement<br>and movement heals</div>
    <div class="hero-name">Lena Marwick<br>Pilates Studio trainer</div>
    <div class="hero-buttons">
      <span class="btn">Price list</span>
      <span class="btn">Timetable</span>
    </div>
  </div>
  <svg class="hero-wave" viewBox="0 0 1200 170" preserveAspectRatio="none">
    <path d="M0 110 C300 40 520 170 800 110 C960 75 1080 60 1200 80 L1200 170 L0 170Z" fill="#c49a45"/>
    <path d="M0 125 C300 55 520 185 800 125 C960 90 1080 75 1200 95 L1200 170 L0 170Z" fill="#ffffff"/>
  </svg>
</header>

<aside class="side-tab">
  <div class="side-tab-body">
    <strong>Einzeltraining / Kurse</strong>
    Private sessions and small studio groups
    <div class="price">€55,00</div>
  </div>
  <div class="side-tab-label">BOOK NOW</div>
</aside>

<section class="offer">
  <h2 class="section-title">What I offer</h2>
  <svg class="title-rule" viewBox="0 0 180 10"><path d="M0 5 H80 M100 5 H180" stroke="#c49a45" stroke-width="1"/><circle cx="90" cy="5" r="3" fill="#c49a45"/></svg>
  <p>The first prerequisite for being able to carry out our every different daily tasks with pleasure and joy is physical fitness, a consciously and trained body and full possession of our motion powers.</p>
  <p>This comprehensive full body training from classic Pilates helps you achieve exactly that. The aim is to achieve optimal performance of the musculoskeletal system – strength, flexibility and endurance – without risk of injury. Pilates originally called his method contrology. The Art of Control. Contrology is the complete coordination of body, mind and spirit. The basic principles form the basis of all Pilates exercises with one goal: movement flows – elegant and secure.</p>
  <span class="btn">Explore more</span>
</section>

<section class="about">
  <svg class="about-wave-top" viewBox="0 0 1200 40" preserveAspectRatio="none"><path d="M0 0 H1200 V10 C900 40 300 0 0 30Z" fill="#ffffff"/></svg>
  <div class="about-photo photo" role="img" aria-label="Portrait of the trainer holding a light dumbbell in the studio"></div>
  <div class="about-caption"><b>Trainer for life</b><span>Pilates private and small groups</span></div>
  <div class="about-text">
    <h2 class="section-title">About me</h2>
    <h3>My philosophy</h3>
    <p>I discovered my love for Pilates several years ago and quickly knew that this was the way I wanted to move and teach. After a long career in the office I completed my training as a Pilates instructor and have never looked back.</p>
    <p>In order to get to know all facets of Pilates, I trained as a studio trainer, both in the classic Pilates method and the modern standard…</p>
    <span class="btn">Read more</span>
  </div>
  <div class="about-photo-2 photo" role="img" aria-label="Trainer performing a stretch on a Pilates reformer"></div>
</section>

<section class="prices">
  <h2 class="section-title">Prices</h2>
  <svg class="title-rule" viewBox="0 0 180 10"><path d="M0 5 H80 M100 5 H180" stroke="#c49a45" stroke-width="1"/><circle cx="90" cy="5" r="3" fill="#c49a45"/></svg>
  <div class="price-grid">
    <div class="price-card">
      <h4>Starter Paket</h4>
      <div class="item"><b>Einzeltraining 2 Stunden</b>Two private lessons for new clients</div>
      <span class="amount">€110,00</span>
      <div class="item">one-time only, valid 4 weeks</div>
    </div>
    <div class="price-card">
      <h4>Einzel/Duett Training</h4>
      <div class="item"><b>Einzel Training 60 Minuten</b>Private session in the studio</div>
      <span class="amount">€55,00 · €65,00</span>
      <div class="item"><b>Duett Training 60 Minuten</b>Two people, one session</div>
      <span class="amount">€80,00 · €90,00</span>
      <div class="item">Studio plus equipment fee included</div>
    </div>
    <div class="price-card">
      <h4>Gruppen Training</h4>
      <div class="item"><b>Gruppentraining 60 Minuten</b>Small groups up to six people</div>
      <span class="amount">€25,00 · €30,00</span>
      <div class="item"><b>Gruppentraining 10er Karte</b>Ten classes, valid six months</div>
      <span class="amount">€220,00</span>
    </div>
    <div class="price-card">
      <h4>Kombi Paket</h4>
      <div class="item"><b>Einzel 5x · Gruppe 5x</b>Mixed package for steady progress</div>
      <span class="amount">€395,00 · €420,00</span>
      <div class="item">Valid three months, freely bookable</div>
    </div>
  </div>
  <div class="price-buttons"><span class="btn">Price list</span><span class="btn">Download timetable</span></div>
</section>

<section class="testimonials">
  <h2 class="section-title">Testimonials</h2>
  <svg class="title-rule" viewBox="0 0 180 10"><path d="M0 5 H80 M100 5 H180" stroke="#c49a45" stroke-width="1"/><circle cx="90" cy="5" r="3" fill="#c49a45"/></svg>
  <div class="quotes">
    <div class="quote">
      <div class="quote-mark">“<small>Apr 02</small></div>
      <p>"A technically excellent Pilates teacher! Each training session includes new exercise sequences with precise instructions, and different small equipment is often used. My summary: definitely try it out, highly recommended. Thank you!"</p>
      <div class="author"><span class="author-dot"></span><div><b>Marlene K.</b><span>Studio client</span></div></div>
    </div>
    <div class="quote">
      <div class="quote-mark">“<small>Apr 02</small></div>
      <p>"Lena is a very good Pilates trainer. She also takes an enormous amount of time for each individual to grasp any long lessons. It makes a lot of fun. That's why I immediately booked her 10 units."</p>
      <div class="author"><span class="author-dot"></span><div><b>Sophie R.</b><span>Group client</span></div></div>
    </div>
  </div>
  <div class="more"><span class="btn">View more</span></div>
  <svg class="test-wave" viewBox="0 0 1200 60" preserveAspectRatio="none"><path d="M0 40 C300 0 700 60 1200 20 V60 H0Z" fill="#ffffff"/></svg>
</section>

<section class="training">
  <div class="training-photo photo" role="img" aria-label="Trainer stretching on a Pilates trapeze table"></div>
  <div class="training-text">
    <h3>Initial and continuing education</h3>
    <ul>
      <li>Pilates Studio Trainer 2019, The Pilates Standard Fundamentals</li>
      <li>Pilates Studio Trainer 2020, Classic Pilates Mat Level 2</li>
      <li>Pilates mat trainer 2018, Body in Motion Pilates Basics</li>
      <li>Several trainer intensive units 2021, Reformer academy</li>
    </ul>
  </div>
  <div class="skills">
    <h3>Personal skills</h3>
    <ul>
      <li>Detailed instructions and corrections</li>
      <li>Motivating participants to tease out their potential through varying sequences</li>
      <li>Strengthen well being</li>
      <li>High demands on professional knowledge through regular training</li>
    </ul>
  </div>
  <div class="training-photo-2 photo" role="img" aria-label="Trainer holding a plank position on a mat"></div>
</section>

<footer class="footer">
  <svg class="footer-wave" viewBox="0 0 1200 60" preserveAspectRatio="none">
    <path d="M0 30 C300 0 800 60 1200 20 V60 H0Z" fill="#c49a45"/>
    <path d="M0 40 C300 10 800 70 1200 30 V60 H0Z" fill="#2c2118"/>
  </svg>
  <div class="footer-logo">Core<br>balance</div>
  <div class="footer-cols">
    <div>
      <h5>Don't miss your workout!</h5>
      <p style="margin-top:8px">Make an appointment for a trial training session today.</p>
      <div class="contact-line"><svg viewBox="0 0 12 12"><path d="M3 1 L5 3 L4 5 C5 7 6 8 7 8 L9 7 L11 9 L10 11 C5 11 1 7 1 2Z" fill="#c49a45"/></svg>+49 160 5512 093</div>
      <div class="contact-line"><svg viewBox="0 0 12 12"><rect x="1" y="3" width="10" height="7" fill="none" stroke="#c49a45"/><path d="M1 3 L6 7 L11 3" fill="none" stroke="#c49a45"/></svg>hello@corebalance-studio.com</div>
    </div>
    <div>
      <h6>Studio address Marienfeld</h6>
      <p>Lindenstraße 14<br>83646 Brennach<br>Mo – Fr 8:00 – 20:00</p>
    </div>
    <div>
      <h6>Studio address Unterwald</h6>
      <p>Bergweg 7a<br>83661 Unterwald<br>Di + Do 9:00 – 19:00</p>
    </div>
    <div>
      <h6>Quick links</h6>
      <p>Home<br>Trainings<br>About me<br>Contact</p>
    </div>
    <div class="badge" role="img" aria-label="Certificate badge"></div>
  </div>
  <div class="footer-bottom">
    <span>© 2024 Corebalance Studio. All Rights Reserved.</span>
    <span>Privacy Notice · Imprint · corebalance-studio.com</span>
    <div class="socials"><i></i><i></i><i></i></div>
  </div>
</footer>

</body>
</html>
```